Business Card Design Project

We are looking to redesign the logo, business card and stationary of one of our group companies - KESTRAL SUPPLY COMPANY LLC.

The company specialises in industrial PVC and CPVC Piping systems. It is situated in the Middle East and the focus is purely in this region.

The logo work is already completed. The file is uploaded for the reference.

We are looking for a clean minimalistic design for the business card.

regards
Ormund
Updates

Hello Everyone!

Thanks for submitting your designs. 

Yet to find the right design. Probably the below links will give you guys some more idea on what we would like.

Minimalist design with some creativity.

Ormund

http://plaincardgallery.example/inspiration/15-beautifully-minimal-business-cards

http://www.quietlayouthub.example/2011/11/14/30-minimalist-business-card-design/

http://www.firmpixelnotes.example/inspiration/minimal-business-cards/

Target Market(s)

Industrial users

Industry/Entity Type

Industrial

Requirements
Must have
• - Minimalistic design

- Back side of the card should include the manufacturer BRAVOLINE CANADA's decal. The file is upload for the reference

- Further information
Company Name:
KESTRAL SUPPLY COMPANY LLC
Address:
PO Box 9087, Sharjah Industrial Area 5, Qutrani Road
Sharjah, United Arab Emirates
Telephone:
+971-6-5018-392
Fax:
+977-6-5018-393
Email:
mail@ksc-holding.example

- FYI, Kestral Supply Company LLC is the authorised distributor for BRAVOLINE CANADA in the UAE. For further information on bravoline please visit the website www.bravoline.example

```html
<!DOCTYPE html>
<html lang="en">
<head>
<meta charset="utf-8">
<title>Kestral Supply Company LLC – Business Card</title>
<link rel="stylesheet" href="https://fonts.googleapis.com/css2?family=Mulish:wght@400;600;700&display=swap">
<style>
  :root {
    --page-bg: #ece8e1;
    --card-front: #f7f7f5;
    --card-back: #0d0d0d;
    --ink: #141414;
    --ink-soft: #333333;
    --band: #ffffff;
    --mark-grey: #5a5c5e;
    --mark-blue: #3d7ff0;
  }
  * { box-sizing: border-box; margin: 0; padding: 0; }
  html, body {
    width: 1200px; height: 1200px; overflow: hidden;
    background: var(--page-bg);
    font-family: "Mulish", "Century Gothic", sans-serif;
    color: var(--ink);
  }
  .card {
    position: absolute;
    left: 198px; width: 803px; height: 445px;
    box-shadow: 0 2px 6px rgba(0,0,0,0.18);
  }
  .card--front { top: 127px; background: var(--card-front); }
  .card--back  { top: 597px; background: var(--card-back); }

  .holder-name {
    position: absolute; left: 54px; top: 70px;
    font-size: 27px; font-weight: 600; letter-spacing: -0.2px;
  }
  .contact-list {
    position: absolute; left: 54px; top: 243px;
    list-style: none; font-size: 15.5px; line-height: 19px; color: var(--ink-soft);
  }
  .contact-list b { font-weight: 700; color: var(--ink); }
  .company-block {
    position: absolute; left: 54px; top: 341px;
    font-size: 15.5px; line-height: 19.5px; color: var(--ink-soft);
  }
  .company-name { font-weight: 700; color: var(--ink); letter-spacing: 0.3px; }

  .brand-lockup {
    position: absolute; left: 508px; top: 163px; width: 230px; height: 230px;
    display: flex; flex-direction: column; align-items: center; justify-content: center; gap: 14px;
  }
  .brand-square {
    width: 120px; height: 120px; border-radius: 26px;
    background: var(--mark-blue);
  }
  .brand-name { font-size: 22px; font-weight: 600; color: var(--mark-grey); }

  .maker-band {
    position: absolute; left: 373px; top: 185px; width: 430px; height: 80px;
    background: var(--band);
    display: flex; align-items: center; gap: 12px; padding-left: 19px;
  }
  .maker-square { width: 44px; height: 44px; border-radius: 4px; background: var(--card-back); }
  .maker-name { font-size: 30px; font-weight: 700; color: var(--ink); letter-spacing: -0.3px; }
</style>
</head>
<body>
  <section class="card card--front">
    <h1 class="holder-name">Dorian Velasco</h1>
    <ul class="contact-list">
      <li><b>T :</b> +971-6-5018-392</li>
      <li><b>F :</b> +977-6-5018-393</li>
      <li><b>E :</b> mail@ksc-holding.example</li>
    </ul>
    <address class="company-block" style="font-style:normal">
      <div class="company-name">KESTRAL SUPPLY COMPANY LLC</div>
      <div>PO Box 9087, Sharjah Industrial Area 5, Qutrani Road</div>
      <div>Sharjah, United Arab Emirates</div>
    </address>
    <div class="brand-lockup">
      <div class="brand-square"></div>
      <div class="brand-name">Kestral</div>
    </div>
  </section>

  <section class="card card--back">
    <div class="maker-band">
      <div class="maker-square"></div>
      <div class="maker-name">Bravoline Canada</div>
    </div>
  </section>
</body>
</html>
```